Business Card Design for a Private Label Pet Company

We need a business card design for our family-owned company, Hollow Creek Pet Works (www.hollowcreekpetworks.com), out of St. Louis, MO. We provide turnkey private label solutions for retailers, Marketvale sellers and other brands who want to provide high quality, natural, Made in the USA pet products to their customers. Our customer are worldwide and range from the US to the UK to Vietnam and beyond. We offer private label for dozens of pet products including grooming products (shampoos, conditioners, colognes, ear and eye washes, mouthwash, etc.), all meat treats, supplements, and specialty products (pet stain and odor cleaner, anti-chew spray, etc.). We would like to see designs that use the colors, fonts and logos (see variations) within our brand guidelines and fit with the look and feel from our website.

Target Market(s)

Pet Store Owners, Marketvale Sellers, Pet Brand Marketers

Industry/Entity Type

Pet

Contact Information for Business Card

Tom Willoughby
CEO
Hollow Creek Pet Works
5817 Brookhaven Commerce Lane
St. Louis, MO 63521
office: 314.555.0182
mobile: 770.555.0139
email: tom@hollowcreekpetworks.com

Colors

Designer to choose colors to be used in the design.

Requirements
Must have
• Need to follow the brand guidelines attached for colors, fonts and logos
• Need to use the logos attached (or a variation) with our without the tagline
• Name, title, phone (office and mobil), email, address on the business card
• Clean professional look and feel that says: high quality natural pet products, high quality service, made in the USA
Nice to have
• Made in the USA is a big positive in our industry and we are very proud of it. There is an attached icon from our website. The designer can get creative here as they wish.
• I do like using color for pop. Just don't like lots of bright, loud colors.
Should not have
• lots of bright, loud colors
• overwhelming to the reader
• crowded

```html
<!DOCTYPE html>
<html lang="en">
<head>
<meta charset="utf-8">
<title>Hollow Creek Pet Works — Business Card</title>
<link rel="stylesheet" href="https://fonts.googleapis.com/css2?family=Lato:wght@300;400;700&display=swap">
<style>
  :root {
    --backdrop: #e9e7e2;
    --front-green: #6e8640;
    --paw-tint: #b0bd90;
    --back-slate: #4f6766;
    --ink-light: #ffffff;
    --badge-ring: #8e9c9b;
    --badge-fill: #5d7473;
  }
  * { box-sizing: border-box; margin: 0; padding: 0; }
  html, body { width: 1200px; height: 1200px; overflow: hidden; }
  body {
    background: var(--backdrop);
    font-family: "Lato", sans-serif;
    color: var(--ink-light);
    position: relative;
  }
  .card {
    position: absolute;
    left: 180px;
    width: 840px;
    height: 480px;
    border-radius: 6px;
    box-shadow: 0 10px 30px rgba(0,0,0,0.18);
    overflow: hidden;
  }
  .card--front { top: 90px; background: var(--front-green); }
  .card--back  { top: 630px; background: var(--back-slate); }

  .paw-decoration {
    position: absolute;
    left: 50px;
    top: 40px;
    width: 340px;
    height: 320px;
  }
  .brand-name {
    position: absolute;
    right: 56px;
    bottom: 56px;
    font-weight: 700;
    font-size: 26px;
    letter-spacing: 0.5px;
    line-height: 1;
    white-space: nowrap;
    text-transform: uppercase;
    color: var(--ink-light);
  }

  .contact-block { position: absolute; left: 70px; top: 60px; width: 440px; }
  .person-name { font-weight: 400; font-size: 44px; line-height: 1; }
  .person-title { font-weight: 400; font-size: 22px; margin-top: 6px; }
  .rule { height: 2px; background: var(--ink-light); margin: 24px 0 22px; }
  .contact-list { list-style: none; }
  .contact-list li {
    display: flex; align-items: center;
    font-size: 22px; line-height: 1; margin-bottom: 16px;
    white-space: nowrap;
  }
  .contact-list svg { width: 26px; height: 26px; margin-right: 14px; flex: none; }
  .contact-list .sep { margin-right: 12px; }
  .address { font-size: 20px; line-height: 1.3; font-weight: 400; }

  .usa-badge {
    position: absolute;
    right: 70px;
    top: 130px;
    width: 240px;
    height: 240px;
  }
</style>
</head>
<body>

<section class="card card--front" aria-label="Card front">
  <svg class="paw-decoration" viewBox="0 0 340 320" role="img" aria-label="Large faint paw print decoration">
    <rect x="0" y="0" width="340" height="320" rx="110" fill="var(--paw-tint)" opacity="0.55"/>
  </svg>
  <div class="brand-name">Hollow Creek Pet Works</div>
</section>

<section class="card card--back" aria-label="Card back">
  <div class="contact-block">
    <h1 class="person-name">Tom Willoughby</h1>
    <p class="person-title">CEO</p>
    <div class="rule"></div>
    <ul class="contact-list">
      <li>
        <svg viewBox="0 0 24 24" aria-hidden="true"><path fill="#fff" d="M3 8c0-2 2-3 9-3s9 1 9 3v2h-5V8H8v2H3zM6 11h12l2 8H4z"/><circle cx="12" cy="15" r="2" fill="var(--back-slate)"/></svg>
        <span class="sep">:</span>314.555.0182
      </li>
      <li>
        <svg viewBox="0 0 24 24" aria-hidden="true"><circle cx="12" cy="12" r="10" fill="none" stroke="#fff" stroke-width="1.8"/><path fill="#fff" d="M9 6.5l2 2.5-1.2 1.3c.7 1.6 1.8 2.8 3.4 3.6l1.3-1.2 2.5 2-1.3 2c-4-.5-7.6-4.2-8.2-8.2z"/></svg>
        <span class="sep">:</span>770.555.0139
      </li>
      <li>
        <svg viewBox="0 0 24 24" aria-hidden="true"><rect x="2" y="5" width="20" height="14" fill="none" stroke="#fff" stroke-width="1.8"/><path d="M2 5l10 8 10-8" fill="none" stroke="#fff" stroke-width="1.8"/></svg>
        <span class="sep">:</span>tom@hollowcreekpetworks.com
      </li>
    </ul>
    <div class="rule"></div>
    <p class="address">Hollow Creek Pet Works<br>5817 Brookhaven Commerce Lane,<br>St. Louis, MO 63521</p>
  </div>

  <svg class="usa-badge" viewBox="0 0 240 240" role="img" aria-label="Made in the USA seal with flag">
    <circle cx="120" cy="120" r="116" fill="none" stroke="var(--badge-ring)" stroke-width="4"/>
    <circle cx="120" cy="120" r="82" fill="var(--badge-fill)"/>
  </svg>
</section>

</body>
</html>
```